Rock band business card design

I need an edgy double sided business card to hand out at music events and to send out to radio.

It needs to display our logo, web address and social media icons (plazzo, chirpex, sonicvaultly).

Colour scheme to match our website (www.torvelkash.com)

Please include this quote:
Bright embers rising... a stirring... TORVEL KASH.

Logo files have been attached.

I look forward to seeing your designs!

Target Market(s)

radio stations, music fans.

Industry/Entity Type

Events

Requirements
Must have
• Website address, social media icons, quote, colour scheme to match www.torvelkash.com

```html
<!DOCTYPE html>
<html lang="en">
<head>
<meta charset="utf-8">
<title>Torvel Kash – Business Card</title>
<link rel="stylesheet" href="https://fonts.googleapis.com/css2?family=Arimo:wght@400;700&family=Cinzel:wght@600&display=swap">
<style>
  :root {
    --black: #050505;
    --gold: #b8904a;
    --gold-light: #e0bd73;
    --gold-dark: #7a5a24;
    --sky-top: #7a3a12;
    --sky-mid: #e0861e;
    --sky-glow: #ffd45a;
    --sand: #b9782e;
    --genre: #e4d35e;
    --white: #ffffff;
    --ink: #1a0e05;
    --icon: #3a3a3a;
  }
  html, body {
    margin: 0;
    padding: 0;
    width: 1200px;
    height: 686px;
    overflow: hidden;
    background: var(--black);
  }
  .card {
    position: relative;
    width: 1200px;
    height: 686px;
    background: var(--black);
    font-family: "Arimo", Arial, sans-serif;
    overflow: hidden;
  }
  .gold-rule {
    position: absolute;
    left: 0;
    width: 1200px;
    height: 7px;
    background: linear-gradient(180deg, var(--gold-light), var(--gold) 50%, var(--gold-dark));
  }
  .gold-rule--top { top: 50px; }
  .gold-rule--bottom { top: 617px; }

  .hero {
    position: absolute;
    left: 0;
    top: 86px;
    width: 1200px;
    height: 434px;
    background:
      radial-gradient(ellipse 380px 260px at 790px 300px, var(--sky-glow) 0%, rgba(255,212,90,0.55) 40%, rgba(255,212,90,0) 75%),
      linear-gradient(180deg, var(--sky-top) 0%, var(--sky-mid) 45%, var(--sand) 80%, #5a3410 100%);
  }
  .band-name {
    position: absolute;
    left: 646px;
    top: 88px;
    margin: 0;
    font-family: "Cinzel", Georgia, serif;
    font-weight: 600;
    font-size: 44px;
    letter-spacing: 1px;
    color: var(--ink);
    line-height: 1;
  }
  .genre {
    position: absolute;
    left: 55px;
    top: 404px;
    margin: 0;
    font-weight: 700;
    font-size: 34px;
    color: var(--genre);
    text-shadow: -1px -1px 0 #2a1a05, 1px -1px 0 #2a1a05, -1px 1px 0 #2a1a05, 1px 1px 0 #2a1a05, 2px 3px 4px rgba(0,0,0,0.7);
    line-height: 1;
  }
  .quote {
    position: absolute;
    left: 349px;
    top: 470px;
    margin: 0;
    font-size: 27px;
    color: var(--white);
    text-shadow: 1px 2px 3px rgba(0,0,0,0.85);
    line-height: 1;
    white-space: nowrap;
  }

  .links {
    position: absolute;
    left: 0;
    top: 520px;
    width: 1200px;
    height: 97px;
    margin: 0;
    padding: 0;
    list-style: none;
  }
  .link {
    position: absolute;
    display: flex;
    align-items: center;
    height: 38px;
    font-weight: 700;
    font-size: 20px;
    color: var(--white);
  }
  .link__mark {
    width: 37px;
    height: 37px;
    margin-right: 18px;
    border-radius: 4px;
    background: var(--icon);
  }
  .link--plazzo { left: 57px; top: 7px; }
  .link--chirpex { left: 57px; top: 53px; }
  .link--sonicvaultly { left: 586px; top: 7px; }
  .link--tunestall { left: 586px; top: 53px; }

  .website {
    position: absolute;
    left: 0;
    top: 633px;
    width: 1200px;
    margin: 0;
    text-align: center;
    font-weight: 700;
    font-size: 25px;
    color: var(--white);
    line-height: 1;
  }
</style>
</head>
<body>
  <main class="card">
    <div class="gold-rule gold-rule--top"></div>

    <section class="hero" role="img" aria-label="Photograph of the Giza pyramids against a glowing orange desert sunset"></section>

    <h1 class="band-name">TORVEL KASH</h1>
    <p class="genre">Rock / Melodic Rock / Experimental</p>
    <p class="quote">Bright embers rising... a stirring... TORVEL KASH.</p>

    <ul class="links">
      <li class="link link--plazzo"><span class="link__mark"></span>https://www.plazzo.com/torvelkash</li>
      <li class="link link--chirpex"><span class="link__mark"></span>https://chirpex.com/torvelkash</li>
      <li class="link link--sonicvaultly"><span class="link__mark"></span>http://www.sonicvaultly.com/torvelkash</li>
      <li class="link link--tunestall"><span class="link__mark"></span>http://torvelkash.tunestall.com</li>
    </ul>

    <div class="gold-rule gold-rule--bottom"></div>

    <p class="website">www.torvelkash.com</p>
  </main>
</body>
</html>
```